Harborline Energy - needs a business card

Harborline Energy is a U.S. based diesel sourcing and distribution company that supports American oil & gas fields through providing quality product and consistent services.

Target Market(s)

Oil and Gas

Contact Information for Business Card

The background of the card must be white to ensure the logo pops.

Font styles to use
Serif
Sans Serif

Colors

Designer to choose colors to be used in the design.

Requirements
Must have
• Front of Card: Tag line: Harborline Energy, Powering America's Oil & Gas fields.
• Not sure if you guys do this part but just in case...
• Dale Menschow
• Owner/CEO
• C:555.318.4076
• E:Dmenschow@harborlineenergy.example
• W:Harborlineenergy.example
• Locations: Servicing the Powder River, DJ basin and Bakken formations.
• Back of Card: " Frac fueling is what we do. We understand how important diesel fuel is to your operation, which is why our main service line is Frac fueling. We assure our supply and stand by our service"

```html
<!DOCTYPE html>
<html lang="en">
<head>
<meta charset="utf-8">
<title>Harborline Energy – Business Card</title>
<link href="https://fonts.googleapis.com/css2?family=Source+Sans+3:wght@400;600;700&family=Source+Serif+4:ital,wght@0,400;1,400&display=swap" rel="stylesheet">
<style>
  :root {
    --navy: #1f2d66;
    --red: #c3262d;
    --icon-blue: #2e3c8f;
    --rule: #4a4a4a;
    --muted: #4a5175;
    --paper: #ffffff;
    --page: #ffffff;
  }
  html, body {
    margin: 0;
    padding: 0;
    width: 1200px;
    height: 1200px;
    overflow: hidden;
    background: var(--page);
    font-family: "Source Sans 3", sans-serif;
  }
  .card {
    position: absolute;
    left: 254px;
    width: 694px;
    height: 396px;
    background: var(--paper);
    box-shadow: 0 1px 4px rgba(0,0,0,0.28);
  }
  .card--front { top: 112px; }
  .card--back { top: 611px; }

  .brand {
    position: absolute;
    display: flex;
    flex-direction: column;
    align-items: center;
    color: var(--navy);
    font-weight: 700;
    white-space: nowrap;
  }
  .brand__dot {
    border-radius: 50%;
    background: var(--navy);
  }
  .brand--large {
    left: 0;
    right: 0;
    top: 110px;
    font-size: 28px;
    gap: 12px;
  }
  .brand--large .brand__dot { width: 70px; height: 70px; }
  .brand--small {
    left: 34px;
    top: 38px;
    width: 84px;
    font-size: 12px;
    gap: 8px;
  }
  .brand--small .brand__dot { width: 42px; height: 42px; }

  .tagline {
    position: absolute;
    left: 0;
    right: 0;
    top: 240px;
    margin: 0;
    text-align: center;
    font-family: "Source Serif 4", serif;
    font-style: italic;
    font-size: 15px;
    color: var(--red);
  }
  .service-statement {
    position: absolute;
    left: 97px;
    width: 500px;
    bottom: 28px;
    margin: 0;
    text-align: center;
    font-family: "Source Serif 4", serif;
    font-size: 12px;
    line-height: 1.45;
    color: var(--muted);
  }
  .service-statement__lead {
    font-family: "Source Sans 3", sans-serif;
    font-weight: 700;
    color: var(--navy);
  }

  .holder__name {
    position: absolute;
    right: 49px;
    top: 144px;
    margin: 0;
    font-size: 22px;
    font-weight: 400;
    color: var(--navy);
  }
  .holder__rule {
    position: absolute;
    left: 0;
    top: 183px;
    width: 546px;
    height: 1px;
    background: var(--rule);
  }
  .holder__title {
    position: absolute;
    right: 48px;
    top: 177px;
    margin: 0;
    font-size: 15px;
    color: var(--red);
  }
  .contact {
    position: absolute;
    right: 34px;
    display: flex;
    align-items: center;
    gap: 14px;
    font-size: 18px;
    color: var(--red);
  }
  .contact--phone { top: 245px; }
  .contact--email { top: 282px; }
  .contact--web { top: 319px; }
  .contact__icon {
    width: 24px;
    height: 24px;
    flex: none;
    fill: none;
    stroke: var(--icon-blue);
    stroke-width: 1.6;
  }
  .locations {
    position: absolute;
    left: 34px;
    bottom: 30px;
    width: 240px;
    margin: 0;
    font-size: 13px;
    line-height: 1.35;
    color: var(--navy);
  }
</style>
</head>
<body>

<section class="card card--front" aria-label="Card front">
  <div class="brand brand--large">
    <span class="brand__dot"></span>
    <span class="brand__name">Harborline Energy</span>
  </div>
  <p class="tagline">Harborline Energy, Powering America's Oil &amp; Gas fields.</p>
  <p class="service-statement"><span class="service-statement__lead">Frac fueling is what we do.</span> We understand how important diesel fuel is to your operation, which is why our main service line is Frac fueling. We assure our supply and stand by our service.</p>
</section>

<section class="card card--back" aria-label="Card back">
  <div class="brand brand--small">
    <span class="brand__dot"></span>
    <span class="brand__name">Harborline Energy</span>
  </div>

  <h1 class="holder__name">Dale Menschow</h1>
  <div class="holder__rule"></div>
  <p class="holder__title">Owner/CEO</p>

  <div class="contact contact--phone">
    <span>555 318 4076</span>
    <svg class="contact__icon" viewBox="0 0 24 24" aria-hidden="true">
      <path d="M5 3 L9 3 L10.5 7.5 L8.3 9.2 C9.5 11.8 12 14.4 14.8 15.7 L16.5 13.5 L21 15 L21 19 C21 20 20 21 19 21 C10.5 20.5 3.5 13.5 3 5 C3 4 4 3 5 3 Z"/>
    </svg>
  </div>
  <div class="contact contact--email">
    <span>Dmenschow@harborlineenergy.example</span>
    <svg class="contact__icon" viewBox="0 0 24 24" aria-hidden="true">
      <rect x="2" y="5" width="20" height="14"/>
      <path d="M2 5 L12 13 L22 5 M2 19 L9.5 11 M22 19 L14.5 11"/>
    </svg>
  </div>
  <div class="contact contact--web">
    <span>Harborlineenergy.example</span>
    <svg class="contact__icon" viewBox="0 0 24 24" aria-hidden="true">
      <circle cx="12" cy="12" r="10"/>
      <path d="M4.9 4.9 L19.1 19.1 M19.1 4.9 L4.9 19.1 M12 2 C15 6 15 18 12 22"/>
    </svg>
  </div>

  <p class="locations">Servicing the Powder River, DJ basin and Bakken formations.</p>
</section>

</body>
</html>
```